Web Design Project

8 page static website.
About us/What we stand for:
Forno Verde CBD plans to make a huge splash in Sydney by being the first Italian pizza and pasta retail food outlet offering truly fresh, nutritious ingredients – herbs and vegetables are picked directly from the garden, pizzas are made with love in a fun filled atmosphere and a cutting edge brand strategy that promotes a happy lifestyle and reminds people that happiness and togetherness comes from sharing amazing food.
The best thing about Forno Verde is that it offers consumers a choice to either choose from the enticing gluten free and vegetarian menu range to the more traditional pizza and pasta, we cater for their own tastes, this provides a distinct point of difference in the retail food market, as well as allowing consumers to have an endless range of choices without having to worry about the nutritional value.
Consumers have now become accustomed to a consistent brand experience which is setting increasingly high standards when it comes to food quality, taste and service.
We want to capitalise on the opportunity to create a strong, modern brand that promotes healthy lifestyle habits, sells fresh, wholesome ingredients, delivers
exceptional service in a fun filled atmosphere and appeals to a broad market.
Our business model is specifically pickup and delivery with a few seats and crates for eating in. It is for the time poor that still want to have a great tasting Italian experience with pizza and pasta within the quick service restaurant space. Takeaway, office catering and delivery will be a large percentage of our business.
Our philosophy at Forno Verde is simple:
“Success is not a formula, it’s a recipe”.
Brand personality:
We are located in a laneway and basically the shop is a hole in the one. It looks like a restaurant you would see in Italy.
Modern Italian, contemporary, fun, rustic (Taco Rondo, Brasa’t)
1 Aims of this website
• Emotionally connect with the target audience to reflect (“happiness and togetherness comes from sharing amazing food”)
• To entice people to order pizza
• To capture a mailing list
• To differentiate us from the low cost, low quality pizza
• To create a connection with the target audience, and promote word of mouth
2 Target audience(s)
• Male/Female
• 18-49
• Sydney CBD and Pemberly Quay
• Internet Savvy.
3. Contents/Functionality
www.crustwagon.com.au – like the rustic brown in the website and the old washed out white colour through the font.
Target Market(s)
18-49 years old
City worker and resident
people that enjoy good food
Industry/Entity Type
Restaurant
Requirements
Must have
- Some splash of red and green to represent the italian theme.
Attached is a draft of the homepage layout.
Attached below are some fonts that we like.
Nice to have
- Please see http://www.brasat.com.au/Pages/locationmenu.aspx
This is how our takeaway menu looks like.

```html
<!DOCTYPE html>
<html lang="en">
<head>
<meta charset="utf-8">
<title>Forno Verde – Home</title>
<link href="https://fonts.googleapis.com/css2?family=Playball&family=Tinos&family=Ubuntu:wght@400;500&display=swap" rel="stylesheet">
<style>
:root{
  --page-dark:#3a150c;
  --page-mid:#5a2314;
  --column:#6e2a17;
  --header:#7c2f1b;
  --slider-top:#5c2414;
  --slider-bottom:#3b170d;
  --nav-light:#f4f4f4;
  --nav-dark:#c9c9c9;
  --nav-text:#6b2415;
  --cream:#f7e7c4;
  --white:#ffffff;
  --gold-light:#f3c528;
  --gold-dark:#d9a300;
  --heading-dark:#3a1206;
  --parchment:#d9a56b;
  --parchment-light:#f0cfa0;
  --parchment-edge:#b67a3e;
  --scroll-text:#4a1c0b;
  --field:#efc78e;
  --button:#4a1608;
  --dot-grey:#a8a8a8;
  --dot-active:#e4b100;
  --footer-top:#f2c313;
  --footer-bottom:#c98f00;
  --footer-text:#3a1a08;
  --italy-green:#2f8f3a;
  --italy-red:#c8261d;
}
*{box-sizing:border-box;margin:0;padding:0}
html,body{width:1029px;height:1200px;overflow:hidden}
body{
  position:relative;
  background:linear-gradient(90deg,var(--page-dark) 0,var(--page-mid) 8.5%,var(--page-mid) 91.5%,var(--page-dark) 100%);
  font-family:"Tinos",serif;
}
.column{
  position:absolute;left:88px;top:0;width:855px;height:1128px;
  background:linear-gradient(180deg,var(--header) 0,var(--column) 50%,#4a1b0e 100%);
}
.social{position:absolute;left:800px;top:42px;display:flex;gap:6px}
.social span{width:28px;height:28px;border-radius:6px;display:block}
.social .s1{background:#f08a1c}.social .s2{background:#3b5a9a}
.social .s3{background:#d8d8d8}.social .s4{background:#4bb7e6}

.nav{
  position:absolute;left:88px;top:90px;width:853px;height:64px;
  background:linear-gradient(180deg,var(--nav-light),var(--nav-dark));
}
.nav ul{list-style:none;position:absolute;left:350px;top:0;display:flex;height:64px}
.nav li{
  width:126px;height:64px;display:flex;align-items:center;justify-content:center;
  font-family:"Playball",cursive;font-size:21px;color:var(--nav-text);
  border-left:2px solid #b5b5b5;
}
.nav li:first-child{border-left:none;width:124px}

.logo{
  position:absolute;left:148px;top:69px;width:138px;height:114px;
  background:var(--white);border-radius:10px;
  box-shadow:2px 4px 6px rgba(0,0,0,.45);
  display:flex;flex-direction:column;align-items:center;justify-content:center;gap:8px;
}
.logo .mark{width:26px;height:26px;border-radius:50%;background:var(--italy-green)}
.logo .name{font-family:"Playball",cursive;font-size:22px;color:var(--italy-green)}

.slider{
  position:absolute;left:88px;top:180px;width:855px;height:370px;border-radius:12px;
  background:linear-gradient(180deg,var(--slider-top),var(--slider-bottom));
}
.slide-photo{
  position:absolute;left:32px;top:39px;width:566px;height:298px;border-radius:8px;
  background:radial-gradient(ellipse at 45% 45%,#d98a3a 0,#a8471f 45%,#4a1a0b 100%);
}
.slide-copy{position:absolute;left:626px;top:48px;width:210px;color:var(--cream);font-family:"Playball",cursive}
.slide-copy h2{font-weight:400;font-size:28px;color:#f3d49b;margin-bottom:16px}
.slide-copy p{font-size:19px;line-height:31px;color:var(--white);margin-bottom:13px}
.dots{position:absolute;left:740px;top:329px;display:flex;gap:10px}
.dots span{width:18px;height:18px;border-radius:50%;background:var(--dot-grey)}
.dots .active{background:var(--dot-active)}

.label{
  position:absolute;width:170px;height:51px;
  background:linear-gradient(180deg,var(--gold-light),var(--gold-dark));
  font-family:"Playball",cursive;font-size:28px;color:var(--heading-dark);
  padding-left:12px;line-height:51px;
}
.welcome-label{left:113px;top:577px}
.testimonial-label{left:727px;top:585px}
.welcome-text{
  position:absolute;left:120px;top:646px;width:594px;
  color:var(--white);font-size:12px;line-height:30.5px;text-align:justify;text-align-last:justify;
}
.testimonial-text{
  position:absolute;left:728px;top:648px;width:210px;
  font-family:"Playball",cursive;font-size:19px;line-height:31px;color:var(--white);
}

.scroll{position:absolute;top:840px;width:154px;height:240px}
.scroll svg{position:absolute;inset:0}
.scroll-body{position:absolute;left:0;top:0;width:154px;height:240px}
.order{left:141px}.club{left:331px}.catering{left:535px}.delivery{left:724px}
.ph{position:absolute}
.order .ph{left:10px;top:45px;width:132px;height:124px;background:linear-gradient(135deg,#6a5a55,#2a2230 60%,#1b1620)}
.order .cta{position:absolute;left:26px;top:174px;font-family:"Ubuntu",sans-serif;font-size:13px;line-height:17px;color:var(--scroll-text);text-align:center}
.order .arrow{position:absolute;left:112px;top:180px}
.club .title{position:absolute;left:14px;top:44px;font-family:"Ubuntu",sans-serif;font-size:12.5px;color:var(--scroll-text)}
.club .lbl{position:absolute;left:18px;font-family:"Ubuntu",sans-serif;font-size:12.5px;color:var(--scroll-text)}
.club .field{position:absolute;left:16px;width:119px;height:27px;background:var(--field);border:1px solid #6b3a1a}
.club .go{position:absolute;left:92px;top:183px;width:39px;height:25px;border-radius:7px;background:var(--button);color:var(--white);font-family:"Ubuntu",sans-serif;font-size:13px;text-align:center;line-height:25px}
.catering .ph{left:13px;top:45px;width:128px;height:96px;border:2px solid #6a2a14;background:linear-gradient(180deg,#c9c2b8,#5e5a58)}
.delivery .ph{left:16px;top:52px;width:122px;height:97px;background:linear-gradient(135deg,#efe6d0,#e8d6b6)}
.scroll .caption{position:absolute;left:0;width:154px;text-align:center;font-family:"Ubuntu",sans-serif;font-weight:500;font-size:18px;line-height:21px;color:var(--scroll-text)}

.footer{
  position:absolute;left:0;top:1128px;width:1029px;height:72px;
  background:linear-gradient(180deg,var(--footer-top),var(--footer-bottom));
  font-family:"Ubuntu",sans-serif;font-size:16px;color:var(--footer-text);
}
.footer .links{position:absolute;left:101px;top:22px}
.footer .copy{position:absolute;right:104px;top:22px}
</style>
</head>
<body>
<div class="column"></div>

<div class="social" aria-label="Social links">
  <span class="s1"></span><span class="s2"></span><span class="s3"></span><span class="s4"></span>
</div>

<nav class="nav">
  <ul><li>Home</li><li>About Us</li><li>Menus</li><li>Contact Us</li></ul>
</nav>

<div class="logo"><span class="mark"></span><span class="name">Forno Verde</span></div>

<section class="slider">
  <div class="slide-photo" role="img" aria-label="Close-up of a hand lifting a slice of loaded pizza"></div>
  <div class="slide-copy">
    <h2>Lorum Ipsum</h2>
    <p>Lorem Ipsum is simply dummy text of the printing and typeset-ting industry</p>
    <p>Lorem Ipsum is simply dummy text of the printing and typeset-ting industry</p>
  </div>
  <div class="dots"><span></span><span class="active"></span><span></span></div>
</section>

<h2 class="label welcome-label">Welcome</h2>
<p class="welcome-text">Lorem Ipsum is simply dummy text of the printing and typesetting industry. Lorem Ipsum has been the industry's standard dummy text ever since the 1500s, when an unknown printer took a galley of type and scrambled it to make a type specimen book. It has survived not only five centuries, but also the leap into electronic typesetting, remaining essentially unchanged. It was popularised in the 1960s with the release of Letterpage sheets containing Lorem Ipsum passages, and more recently with</p>

<h2 class="label testimonial-label">Testimonials</h2>
<p class="testimonial-text">Lorem Ipsum is simply dummy text of the printing and typeset-ting industry</p>

<svg width="0" height="0" style="position:absolute">
  <defs>
    <linearGradient id="parch" x1="0" x2="1">
      <stop offset="0" stop-color="#c98e52"/><stop offset=".5" stop-color="#f0cfa0"/><stop offset="1" stop-color="#c98e52"/>
    </linearGradient>
    <symbol id="scroll-shape" viewBox="0 0 154 240">
      <rect x="6" y="14" width="142" height="212" fill="url(#parch)" stroke="#9c6330" stroke-width="1.5"/>
      <rect x="0" y="2" width="154" height="22" rx="11" fill="url(#parch)" stroke="#9c6330" stroke-width="1.5"/>
      <rect x="0" y="216" width="154" height="22" rx="11" fill="url(#parch)" stroke="#9c6330" stroke-width="1.5"/>
      <ellipse cx="8" cy="13" rx="6" ry="9" fill="#b57a3d"/>
      <ellipse cx="146" cy="13" rx="6" ry="9" fill="#b57a3d"/>
      <ellipse cx="8" cy="227" rx="6" ry="9" fill="#b57a3d"/>
      <ellipse cx="146" cy="227" rx="6" ry="9" fill="#b57a3d"/>
    </symbol>
  </defs>
</svg>

<div class="scroll order">
  <svg class="scroll-body" viewBox="0 0 154 240"><use href="#scroll-shape"/></svg>
  <div class="ph" role="img" aria-label="Pizza beside a tablet showing the online order screen"></div>
  <div class="cta">Click Here To<br>Order Online</div>
  <svg class="arrow" width="30" height="20" viewBox="0 0 30 20"><path d="M0 10 L12 0 V6 H30 V14 H12 V20 Z" fill="#4a1608"/></svg>
</div>

<div class="scroll club">
  <svg class="scroll-body" viewBox="0 0 154 240"><use href="#scroll-shape"/></svg>
  <div class="title">Join Our Email – Club</div>
  <div class="lbl" style="top:73px">Name:</div>
  <div class="field" style="top:94px"></div>
  <div class="lbl" style="top:126px">Email:</div>
  <div class="field" style="top:149px"></div>
  <div class="go">GO</div>
</div>

<div class="scroll catering">
  <svg class="scroll-body" viewBox="0 0 154 240"><use href="#scroll-shape"/></svg>
  <div class="ph" role="img" aria-label="Interior of the restaurant dining area"></div>
  <div class="caption" style="top:154px">Office<br>Caterring</div>
</div>

<div class="scroll delivery">
  <svg class="scroll-body" viewBox="0 0 154 240"><use href="#scroll-shape"/></svg>
  <div class="ph" role="img" aria-label="Street map of the delivery area"></div>
  <div class="caption" style="top:166px">Delivery Area</div>
</div>

<footer class="footer">
  <div class="links">Home | About Us |&nbsp; Menu’s | Contact Us</div>
  <div class="copy">Copyright@2011</div>
</footer>
</body>
</html>
```